Music Festival in Colorado Needs Awesome Flier Design

We need an eye-catching & captivating flier design for an annual music festival in Denver, CO (USA). The festival features the best Colorado musicians within the genres of jam - funk - bluegrass - electronic - reggae - rock.

The design should look clean and professional while still being creative and unique. The past three years' flier designs are attached, as well as the logo and some other designs that match the aesthetic of what we're looking for.

This festival has a big element of Colorado pride so any

Target Market(s)

Hippies - live music enthusiasts - partiers. Ages 21 - 40.

Industry/Entity Type

Entertainment

Colors
0355a3
ec1f27
ffffff
fbed22

Requirements
Must have
• Attached design text.
Nice to have
• - Quality texture and psychedelic elements.
• - Colorado pride elements; color scheme (red, white, blue & yellow), flag, ect.
• - Nature elements are awesome but this is also a downtown festival so keep that in mind.
Should not have
• Cheesy artwork.

```html
<!DOCTYPE html>
<html lang="en">
<head>
<meta charset="utf-8">
<title>Echo Ridge Music Festival</title>
<link rel="stylesheet" href="https://fonts.googleapis.com/css2?family=Bebas+Neue&family=Lato:wght@400;700&family=Montserrat:wght@800&display=swap">
<style>
  :root {
    --red: #ec1f27;
    --blue: #0355a3;
    --ink: #141414;
    --white: #ffffff;
    --stage: #3a3a3a;
    --mist: #e4dcdc;
    --sky-blue: #c9d9ec;
    --warm: #e98a6e;
    --ember: #d2472f;
  }
  * { margin: 0; padding: 0; box-sizing: border-box; }
  html, body { width: 1200px; height: 1200px; overflow: hidden; }
  body { background: var(--stage); position: relative; }

  .flier {
    position: absolute; left: 172px; top: 0;
    width: 856px; height: 1200px; overflow: hidden;
    background:
      radial-gradient(ellipse at 95% 8%, var(--sky-blue) 0%, rgba(201,217,236,0) 45%),
      linear-gradient(175deg, var(--mist) 0%, #e3cfcb 30%, #eaa58e 55%, var(--warm) 70%, var(--ember) 100%);
  }
  .landscape {
    position: absolute; left: 0; right: 0; top: 760px; bottom: 0;
    background:
      linear-gradient(180deg, rgba(236,210,200,0) 0%, #d9b2a5 14%, #9a4a35 32%, #6e2c1f 50%, #b8513c 66%, #8c3a2a 80%, #d06a52 100%);
  }

  .brand {
    position: absolute; top: 60px; left: 0; right: 0;
    display: flex; justify-content: center; align-items: center; gap: 14px;
    font-family: "Bebas Neue", sans-serif; font-size: 96px; line-height: 1;
    color: #2a2a2a; letter-spacing: 2px; white-space: nowrap;
  }
  .brand-mark { width: 18px; height: 18px; background: #2a2a2a; }

  .event-name {
    position: absolute; top: 218px; left: 0; right: 0; text-align: center;
    font-family: "Montserrat", sans-serif; font-weight: 800; font-size: 44px; line-height: 54px;
    color: var(--ink); letter-spacing: 0.5px; white-space: nowrap;
  }

  .date-frame {
    position: absolute; left: 24px; top: 338px; width: 780px; height: 155px;
    border: 3px solid var(--white); border-top: none;
  }
  .frame-top { position: absolute; top: 338px; height: 3px; background: var(--white); }
  .frame-top.left { left: 24px; width: 62px; }
  .frame-top.right { left: 754px; width: 50px; }

  .event-title {
    position: absolute; top: 278px; left: 0; width: 856px; text-align: center;
    font-family: "Bebas Neue", sans-serif; font-size: 134px; line-height: 1;
    color: var(--red); letter-spacing: 0;
    text-shadow: 3px 3px 0 var(--white); white-space: nowrap;
  }

  .event-date {
    position: absolute; top: 418px; left: 84px; height: 52px;
    display: flex; align-items: center; gap: 20px; white-space: nowrap;
    font-family: "Bebas Neue", sans-serif; font-size: 54px; line-height: 1;
    color: var(--ink); letter-spacing: -1px;
  }
  .event-date svg { width: 48px; height: 48px; flex: none; }
  .event-date span { padding-top: 6px; }

  .lineup {
    position: absolute; top: 518px; left: 30px; right: 30px; text-align: center;
    font-family: "Lato", sans-serif; font-size: 17px; line-height: 22px; color: #1e1e1e;
    white-space: nowrap;
  }

  .tickets {
    position: absolute; top: 603px; left: 242px; width: 408px; height: 48px;
  }
  .tickets svg { position: absolute; inset: 0; }
  .tickets span {
    position: absolute; inset: 0; display: flex; align-items: center; justify-content: center;
    font-family: "Bebas Neue", sans-serif; font-size: 36px; letter-spacing: 2px;
    color: var(--white); padding-top: 4px; white-space: nowrap;
  }

  .contact {
    position: absolute; left: 0; right: 0; text-align: center;
    font-family: "Lato", sans-serif; color: #1e1e1e;
    display: flex; justify-content: center; gap: 10px; white-space: nowrap;
  }
  .contact svg { flex: none; }
  .web { top: 665px; font-weight: 700; font-size: 19px; letter-spacing: 2px; align-items: center; }
  .address { top: 704px; font-size: 15px; line-height: 19px; align-items: flex-start; }
</style>
</head>
<body>
  <main class="flier">
    <div class="landscape" role="img" aria-label="Snow-capped Colorado mountains and pine forest reflected in a still lake, tinted red-orange"></div>

    <div class="brand"><span class="brand-mark"></span>Echo Ridge</div>

    <h1 class="event-name">ECHO RIDGE</h1>

    <div class="date-frame"></div>
    <div class="frame-top left"></div>
    <div class="frame-top right"></div>
    <h2 class="event-title">MUSIC FESTIVAL</h2>

    <p class="event-date">
      <svg viewBox="0 0 48 48" aria-hidden="true">
        <circle cx="24" cy="24" r="22" fill="#0355a3" stroke="#fff" stroke-width="3"/>
        <rect x="14" y="15" width="20" height="18" rx="2" fill="none" stroke="#fff" stroke-width="2"/>
        <line x1="14" y1="20" x2="34" y2="20" stroke="#fff" stroke-width="2"/>
        <g fill="#fff">
          <rect x="17" y="23" width="3" height="3"/><rect x="22.5" y="23" width="3" height="3"/><rect x="28" y="23" width="3" height="3"/>
          <rect x="17" y="28" width="3" height="3"/><rect x="22.5" y="28" width="3" height="3"/><rect x="28" y="28" width="3" height="3"/>
        </g>
      </svg>
      <span>MAY 11TH - 13TH, 2018 (6TH ANNUAL)</span>
    </p>

    <p class="lineup">
      Jay Harlan Band, Open Sky Orchestra, Fault Line Theory, The Copper Pines, B-Rae &amp; The Summit,<br>
      Wapiti, Helix, Altitude Ensemble, Cloudspun, Parafonics, Prismatic,<br>
      Clear Drift, Rail Junction, Orbits.
    </p>

    <div class="tickets">
      <svg viewBox="0 0 410 48" preserveAspectRatio="none" aria-hidden="true">
        <path d="M14 4 L396 0 L372 8 L410 10 L380 18 L404 24 L376 30 L400 36 L360 42 L300 48 L0 45 L12 36 L2 28 L16 20 L4 12 Z" fill="#0355a3"/>
      </svg>
      <span>TICKETS &amp; MORE INFO</span>
    </div>

    <p class="contact web">
      <svg width="20" height="20" viewBox="0 0 20 20" aria-hidden="true">
        <circle cx="10" cy="10" r="8" fill="none" stroke="#ec1f27" stroke-width="2"/>
        <ellipse cx="10" cy="10" rx="3.5" ry="8" fill="none" stroke="#ec1f27" stroke-width="1.5"/>
        <line x1="2" y1="10" x2="18" y2="10" stroke="#ec1f27" stroke-width="1.5"/>
      </svg>
      www.echoridgefest.com
    </p>

    <p class="contact address">
      <svg width="14" height="20" viewBox="0 0 14 20" aria-hidden="true">
        <path d="M7 0 C3 0 0 3 0 7 C0 12 7 20 7 20 C7 20 14 12 14 7 C14 3 11 0 7 0 Z" fill="#ec1f27"/>
        <circle cx="7" cy="7" r="2.5" fill="#fff"/>
      </svg>
      <span>Larkspur Yard 418 W. 52nd Ave<br>Denver, CO 80221</span>
    </p>
  </main>
</body>
</html>
```